Digital Marketing Consultant Needs a Business Card Design

I need a business card to brand myself - I'm a digital marketing consultant, and I do web design, SEO, lead generation, social media, etc. I'm overhauling my website (CorinneHalvorsk.com) and just had a snazzy new logo made.

I like the combo of yellow & gray - I find it eye-catching, upbeat and techie. The exact colors of yellow and gray that I like are #F6BF27 and #6D6D6D. But I'm open to suggestions and other color combinations!

I plan on printing the card using some high-end printing techniques that will ensure the card stands out - either really thick cards with colored edges, or spot UV. Not sure which yet, so if you want to incorporate that into your design, that'd be great!

I'm looking for a clean and modern design, but something that will really stand out when paired with 'fancy' printing.

Target Market(s)

Small and medium-sized business owners.

Industry/Entity Type

Printing

Contact Information for Business Card

Corinne Halvorsk
Digital Marketing
Call or Text: 850-555-0927
Corinne@CorinneHalvorsk.com
www.CorinneHalvorsk.com
@QPZ47 on Twitter

Font styles to use
Serif
Sans Serif

Requirements
Must have
• My logo, my contact information, and my "company colors" - #F6BF27 and #6D6D6D.
Nice to have
• If there's room to mention all the things that I do:
• Social Media, Web Design, SEO, Lead Generation, Conversion Funnels, PPC
• (don't add if it makes the card cluttered)

```html
<!DOCTYPE html>
<html lang="en">
<head>
<meta charset="utf-8">
<title>Corinne Halvorsk – Business Card</title>
<link rel="stylesheet" href="https://fonts.googleapis.com/css2?family=Exo+2:wght@400;500;700&display=swap">
<style>
  :root {
    --yellow: #F6BF27;
    --gray: #6D6D6D;
    --band-gray: #8f8f8f;
    --ink: #2b2b2b;
    --paper: #ffffff;
    --backdrop: #e9e9e9;
  }
  html, body {
    margin: 0;
    width: 1200px;
    height: 900px;
    overflow: hidden;
    background: var(--backdrop);
  }
  .stage {
    position: relative;
    width: 1200px;
    height: 900px;
  }
  .card {
    position: absolute;
    left: 150px;
    top: 193px;
    width: 900px;
    height: 514px;
    background: var(--paper);
    overflow: hidden;
    box-shadow: 0 2px 10px rgba(0,0,0,0.12);
    font-family: "Exo 2", sans-serif;
  }
  .card__shapes {
    position: absolute;
    inset: 0;
  }
  .corner-tab {
    position: absolute;
    top: 0;
    right: 24px;
    width: 74px;
    height: 20px;
    background: var(--yellow);
  }
  .contact {
    position: absolute;
    top: 34px;
    right: 40px;
    text-align: right;
    color: var(--ink);
  }
  .contact__name {
    margin: 0 30px 0 0;
    font-size: 27px;
    font-weight: 700;
    letter-spacing: 2px;
    text-transform: uppercase;
  }
  .contact__role {
    margin: 2px 30px 18px 0;
    font-size: 16px;
    font-weight: 500;
  }
  .contact__list {
    list-style: none;
    margin: 0;
    padding: 0;
    font-size: 15px;
    letter-spacing: 1px;
  }
  .contact__item {
    display: flex;
    justify-content: flex-end;
    align-items: center;
    gap: 10px;
    height: 24px;
  }
  .contact__icon {
    width: 16px;
    height: 16px;
    fill: var(--ink);
  }
  .brand {
    position: absolute;
    left: 78px;
    top: 300px;
    display: flex;
    align-items: center;
    gap: 14px;
  }
  .brand__square {
    width: 40px;
    height: 40px;
    border: 3px solid var(--gray);
    box-sizing: border-box;
  }
  .brand__name {
    margin: 0;
    font-size: 26px;
    font-weight: 500;
    letter-spacing: 2px;
    color: var(--gray);
  }
  .address {
    position: absolute;
    left: 40px;
    bottom: 24px;
    margin: 0;
    color: var(--paper);
    font-size: 20px;
    font-weight: 500;
    line-height: 1.35;
    letter-spacing: 1px;
    font-style: normal;
  }
</style>
</head>
<body>
<main class="stage">
  <article class="card">
    <svg class="card__shapes" viewBox="0 0 900 514" width="900" height="514" aria-hidden="true">
      <path d="M0 425 C 320 425, 700 370, 900 255 L900 514 L0 514 Z" fill="var(--band-gray)"/>
      <path d="M520 390 C 690 355, 820 290, 900 215 L900 232 C 825 300, 700 365, 520 390 Z" fill="var(--yellow)"/>
    </svg>

    <div class="corner-tab"></div>

    <section class="contact">
      <h1 class="contact__name">Tobin Varga</h1>
      <p class="contact__role">Managing Director</p>
      <ul class="contact__list">
        <li class="contact__item">012 555 0143
          <svg class="contact__icon" viewBox="0 0 16 16"><path d="M3 1l3 3-1.5 2a9 9 0 0 0 5.5 5.5L12 10l3 3-2 2C7 15 1 9 1 3z"/></svg>
        </li>
        <li class="contact__item">012 555 0143
          <svg class="contact__icon" viewBox="0 0 16 16"><path d="M4 0h8v16H4z M5.5 2v10h5V2z"/></svg>
        </li>
        <li class="contact__item">012 555 0143
          <svg class="contact__icon" viewBox="0 0 16 16"><path d="M4 1h7v4H4z M1 6h14v8H1z M4 9h8v1H4z"/></svg>
        </li>
        <li class="contact__item">hello@mailnest.com
          <svg class="contact__icon" viewBox="0 0 16 16"><path d="M1 3h14v10H1z M2 4l6 5 6-5" stroke="#fff" stroke-width="1"/></svg>
        </li>
        <li class="contact__item">www.yoursitehere.com
          <svg class="contact__icon" viewBox="0 0 16 16"><circle cx="8" cy="8" r="7"/><path d="M1 8h14 M8 1v14 M8 1c-4 4-4 10 0 14 M8 1c4 4 4 10 0 14" stroke="#fff" fill="none"/></svg>
        </li>
      </ul>
    </section>

    <div class="brand">
      <div class="brand__square"></div>
      <p class="brand__name">Corinne Halvorsk</p>
    </div>

    <address class="address">071, 12th floor, Quay<br>Ferngate Road NRV</address>
  </article>
</main>
</body>
</html>
```